Ledge Crafts one page flyer

We need a standard A4 size flyer for a new company called Ledge Crafts. We are a construction material company and sell trims, crown mouldings, baseboards and panelings.
We would like to see the design with the following information:
1. Size: A4
2. Only one front page, no design need to display on back
3. Logo (Ledge Crafts, see the attached EPS file)
4. Slogan: We offer high quality products for competitive prices.
5. Content please see the PDF file
6. The production has 2 category, one called "Crown Moulding", the other is "Wainscoting", Crown Moulding has 5 productions, wainscoting has 2 production(Details see PDF file)
6. We temporary only can provide low resolution images for 7 productions, only the winner will be provided with High Resolution images.
Look and feel
Each slider illustrates characteristics of the customer's brand and the style your logo design should communicate.

```html
<!DOCTYPE html>
<html lang="en">
<head>
<meta charset="UTF-8">
<title>Ledge Crafts – Flyer</title>
<link href="https://fonts.googleapis.com/css2?family=Montserrat:wght@500;600;700&display=swap" rel="stylesheet">
<style>
  :root {
    --page-bg: #e9e9e9;
    --paper: #fafafa;
    --ink-grey: #5d6770;
    --brand-blue: #2352a3;
    --brand-orange: #f05a28;
    --ring-blue: #7f9bd0;
    --ring-orange: #f6a585;
    --footer: #5f6a72;
    --footer-text: #ffffff;
    --icon-grey: #b9c0c5;
  }
  * { margin: 0; padding: 0; box-sizing: border-box; }
  html, body { width: 1200px; height: 1200px; overflow: hidden; }
  body {
    background: var(--page-bg);
    font-family: "Montserrat", sans-serif;
    position: relative;
  }
  .flyer {
    position: absolute;
    left: 160px; top: 30px;
    width: 881px; height: 1140px;
    background: var(--paper);
    box-shadow: 0 6px 24px rgba(0,0,0,0.18);
  }
  .abs { position: absolute; }
  .center { transform: translateX(-50%); white-space: nowrap; text-align: center; }

  .brand {
    left: 440px; top: 28px;
    display: flex; align-items: center; gap: 10px;
  }
  .brand-mark { width: 26px; height: 26px; background: var(--brand-orange); }
  .brand-name {
    font-size: 28px; font-weight: 600; letter-spacing: 1px;
    color: var(--ink-grey); line-height: 1;
  }
  .brand-tagline {
    left: 458px; top: 63px;
    font-size: 9px; font-weight: 500; letter-spacing: 1.6px; color: var(--ink-grey);
  }
  .slogan {
    left: 440px; top: 95px;
    font-size: 20px; font-weight: 500; color: var(--ink-grey);
  }
  .rule-short { left: 0; top: 145px; width: 585px; height: 2px; background: var(--brand-orange); }
  .rule-long { left: 134px; top: 154px; width: 747px; height: 4px; background: var(--brand-orange); }
  .divider { left: 24px; top: 685px; width: 831px; height: 1px; background: var(--brand-orange); }

  .section-title {
    font-size: 28px; font-weight: 700; color: var(--ink-grey); letter-spacing: 0.5px;
  }
  .product { transform: translateX(-50%); width: 300px; text-align: center; }
  .product-name {
    font-size: 15px; font-weight: 700; color: var(--brand-blue);
    text-transform: uppercase; line-height: 1;
  }
  .product-size {
    margin-top: 12px;
    font-size: 22px; font-weight: 700; color: var(--brand-orange); line-height: 1;
  }
  .product-size small { font-size: 16px; }
  .product-visual { display: block; margin: 8px auto 0; width: 140px; height: 140px; }

  .footer-band { left: 0; top: 982px; width: 881px; height: 6px; background: var(--brand-orange); }
  .footer {
    left: 0; top: 988px; width: 881px; height: 152px; background: var(--footer);
  }
  .footer-col { top: 26px; display: flex; gap: 12px; }
  .footer-col svg { flex: none; }
  .footer-text {
    font-size: 14px; font-weight: 600; color: var(--footer-text); line-height: 24px;
  }
  .footer-text.hours { line-height: 29px; margin-top: -4px; }
</style>
</head>
<body>
<main class="flyer">
  <div class="abs brand center">
    <span class="brand-mark"></span>
    <span class="brand-name">LEDGE CRAFTS</span>
  </div>
  <div class="abs brand-tagline center">FOR ALL TYPES OF PROJECTS</div>
  <p class="abs slogan center">WE OFFER HIGH QUALITY PRODUCTS FOR COMPETITIVE PRICES</p>
  <div class="abs rule-short"></div>
  <div class="abs rule-long"></div>

  <h2 class="abs section-title center" style="left:440px;top:182px">CROWN MOULDING</h2>

  <section class="abs product" style="left:151px;top:236px">
    <h3 class="product-name">Brighton 10 Crown Moulding</h3>
    <p class="product-size">8 5/8"<small>x</small>3/4"</p>
    <svg class="product-visual" viewBox="0 0 140 140" role="img" aria-label="Brighton 10 crown moulding profile">
      <circle cx="70" cy="70" r="68" fill="var(--ring-orange)"/>
      <circle cx="70" cy="70" r="64" fill="var(--brand-orange)"/>
    </svg>
  </section>
  <section class="abs product" style="left:439px;top:236px">
    <h3 class="product-name">Brighton 9 Crown Moulding</h3>
    <p class="product-size">7 1/2"<small>x</small>3/4"</p>
    <svg class="product-visual" viewBox="0 0 140 140" role="img" aria-label="Brighton 9 crown moulding profile">
      <circle cx="70" cy="70" r="68" fill="var(--ring-blue)"/>
      <circle cx="70" cy="70" r="64" fill="var(--brand-blue)"/>
    </svg>
  </section>
  <section class="abs product" style="left:729px;top:236px">
    <h3 class="product-name">Brighton 8 Crown Moulding</h3>
    <p class="product-size">6 3/4"<small>x</small>3/4"</p>
    <svg class="product-visual" viewBox="0 0 140 140" role="img" aria-label="Brighton 8 crown moulding profile">
      <circle cx="70" cy="70" r="68" fill="var(--ring-orange)"/>
      <circle cx="70" cy="70" r="64" fill="var(--brand-orange)"/>
    </svg>
  </section>

  <section class="abs product" style="left:300px;top:465px">
    <h3 class="product-name">Aspen 9 Crown Moulding</h3>
    <p class="product-size">7 5/8"<small>x</small>3/4"</p>
    <svg class="product-visual" viewBox="0 0 140 140" role="img" aria-label="Aspen 9 crown moulding profile">
      <circle cx="70" cy="70" r="68" fill="var(--ring-orange)"/>
      <circle cx="70" cy="70" r="64" fill="var(--brand-orange)"/>
    </svg>
  </section>
  <section class="abs product" style="left:588px;top:465px">
    <h3 class="product-name">Aspen 7 Crown Moulding</h3>
    <p class="product-size">6 1/8"<small>x</small>3/4"</p>
    <svg class="product-visual" viewBox="0 0 140 140" role="img" aria-label="Aspen 7 crown moulding profile">
      <circle cx="70" cy="70" r="68" fill="var(--ring-blue)"/>
      <circle cx="70" cy="70" r="64" fill="var(--brand-blue)"/>
    </svg>
  </section>

  <div class="abs divider"></div>

  <h2 class="abs section-title center" style="left:440px;top:707px">WAINSCOTING</h2>

  <section class="abs product" style="left:300px;top:761px">
    <h3 class="product-name">Heritage Chair Rail</h3>
    <p class="product-size">3 1/8"<small>x</small>1"</p>
    <svg class="product-visual" viewBox="0 0 140 140" role="img" aria-label="Heritage chair rail profile">
      <circle cx="70" cy="70" r="68" fill="var(--ring-blue)"/>
      <circle cx="70" cy="70" r="64" fill="var(--brand-blue)"/>
    </svg>
  </section>
  <section class="abs product" style="left:588px;top:761px">
    <h3 class="product-name">Heritage Panel Mould</h3>
    <p class="product-size">1 5/8"<small>x</small>5/8"</p>
    <svg class="product-visual" viewBox="0 0 140 140" role="img" aria-label="Heritage panel mould profile">
      <circle cx="70" cy="70" r="68" fill="var(--ring-orange)"/>
      <circle cx="70" cy="70" r="64" fill="var(--brand-orange)"/>
    </svg>
  </section>

  <div class="abs footer-band"></div>
  <footer class="abs footer">
    <div class="abs footer-col" style="left:26px">
      <svg width="44" height="44" viewBox="0 0 44 44" aria-hidden="true">
        <circle cx="22" cy="22" r="19" fill="none" stroke="var(--icon-grey)" stroke-width="4"/>
        <path d="M22 11v12h9" fill="none" stroke="var(--icon-grey)" stroke-width="4" stroke-linecap="round"/>
      </svg>
      <p class="footer-text hours">Mon – Fri: 7:00am – 6.00pm<br>Saturdays: 8:00am – 4.00pm<br>Sundays: Closed</p>
    </div>
    <div class="abs footer-col" style="left:335px">
      <svg width="32" height="46" viewBox="0 0 32 46" aria-hidden="true">
        <path d="M16 3C8.8 3 3 8.8 3 16c0 10 13 27 13 27s13-17 13-27C29 8.8 23.2 3 16 3z" fill="none" stroke="var(--icon-grey)" stroke-width="3"/>
        <circle cx="16" cy="16" r="5" fill="none" stroke="var(--icon-grey)" stroke-width="3"/>
      </svg>
      <p class="footer-text">Office:<br>214 Maple Crest Rd, unit 7<br>Aurora, Ontario L4G 2K8<br>Phone: 905-555-0142<br>info@ledgecrafts.ca</p>
    </div>
    <div class="abs footer-col" style="left:634px">
      <svg width="40" height="38" viewBox="0 0 40 38" aria-hidden="true">
        <path d="M20 3L2 19h5v16h10V25h6v10h10V19h5z" fill="var(--icon-grey)"/>
      </svg>
      <p class="footer-text">Warehouse:<br>48 Birchmount Way<br>Markham, ON L3R 5T1<br>By Appointment Only</p>
    </div>
  </footer>
</main>
</body>
</html>
```